Private vineyard wine bottle label design

We need a label for our private vineyard's wine in La Cresta California. The wine will not be for sale, so there are no legal requirements about what can or cannot be on the label. We would like the name of the vineyard "Harrow Vine Groves" displayed prominently, and to also include
the grape type "Barbera", and optionally the vineyard location. We would like a stylized (but not cartoonish) image of a stoic bull with horns included. I would also like to hide the image of a maple leaf somewhere on the label, it should be subtle and not obvious unless someone is specifically looking for it. We would like a muted color palate, with a light background.

```html
<!DOCTYPE html>
<html lang="en">
<head>
<meta charset="utf-8">
<title>Harrow Vine Groves – Barbera Label</title>
<link rel="stylesheet" href="https://fonts.googleapis.com/css2?family=EB+Garamond:wght@400;500&family=Pinyon+Script&display=swap">
<style>
  :root {
    --page: #ffffff;
    --label-tan: #c3b59a;
    --ink-navy: #282a38;
    --rule-white: #ffffff;
    --art-top: #2c2e3b;
    --art-bottom: #3e3f4b;
  }
  html, body {
    margin: 0;
    padding: 0;
    width: 1200px;
    height: 1200px;
    overflow: hidden;
    background: var(--page);
  }
  .canvas {
    position: relative;
    width: 1200px;
    height: 1200px;
  }
  .label {
    position: absolute;
    left: 374px;
    top: 134px;
    width: 452px;
    height: 932px;
    border-radius: 226px;
    background: var(--label-tan);
  }
  .label__inner-frame {
    position: absolute;
    inset: 13px;
    border: 1.6px solid var(--rule-white);
    border-radius: 213px;
  }
  .brand {
    position: absolute;
    left: 0;
    right: 0;
    text-align: center;
    color: var(--ink-navy);
  }
  .brand__script {
    top: 276px;
    font-family: "Pinyon Script", cursive;
    font-size: 82px;
    line-height: 1;
    transform: translateX(10px);
  }
  .brand__caps {
    top: 364px;
    font-family: "EB Garamond", serif;
    font-size: 50px;
    line-height: 1;
    letter-spacing: 0.5px;
  }
  .emblem-art {
    position: absolute;
    left: 478px;
    top: 466px;
    width: 220px;
    height: 266px;
  }
  .rule {
    position: absolute;
    height: 1.6px;
    background: var(--ink-navy);
  }
  .rule--upper-left { left: 454px; top: 723px; width: 114px; }
  .rule--upper-right { left: 614px; top: 723px; width: 130px; }
  .rule--lower { left: 454px; top: 802px; width: 290px; }
  .varietal {
    position: absolute;
    left: 454px;
    top: 748px;
    width: 290px;
    text-align: center;
    font-family: "EB Garamond", serif;
    font-size: 33px;
    line-height: 1;
    letter-spacing: 15px;
    padding-left: 15px;
    box-sizing: border-box;
    color: var(--ink-navy);
  }
  .origin {
    position: absolute;
    left: 0;
    right: 0;
    top: 900px;
    text-align: center;
    font-family: "EB Garamond", serif;
    font-size: 18px;
    line-height: 25px;
    letter-spacing: 1px;
    color: var(--ink-navy);
  }
</style>
</head>
<body>
  <main class="canvas">
    <div class="label">
      <div class="label__inner-frame"></div>
    </div>

    <div class="brand brand__script">Harrow</div>
    <div class="brand brand__caps">VINE GROVES</div>

    <svg class="emblem-art" viewBox="0 0 220 266" role="img"
         aria-label="Stylized silhouette of a stoic horned bull's head and shoulders tapering to a point between the rules, with grapevine leaves and grape clusters at its base">
      <defs>
        <linearGradient id="emblemTone" x1="0" y1="0" x2="0" y2="1">
          <stop offset="0%" stop-color="var(--art-top)"/>
          <stop offset="100%" stop-color="var(--art-bottom)"/>
        </linearGradient>
      </defs>
      <path d="M16,0 H204 Q220,0 220,16 V150 C220,200 150,220 122,266 C94,220 0,200 0,150 V16 Q0,0 16,0 Z"
            fill="url(#emblemTone)"/>
    </svg>

    <div class="rule rule--upper-left"></div>
    <div class="rule rule--upper-right"></div>
    <div class="varietal">BARBERA</div>
    <div class="rule rule--lower"></div>

    <div class="origin">LA CRESTA<br>CALIFORNIA</div>
  </main>
</body>
</html>
```